Webdesign für einen  Bauträger und Projektentwickler
Webdesign für einen Bauträger und Projektentwickler
Zielgruppe
Wir sind ein Bauträger und Projektentwickler aus Ulm. Kapitalanleger sind hauptsächlich unsere Zielgruppe.
Aufgabenstellung
Die bereits bestehende Webseite soll überarbeitet werden bzw. das Design & Layout soll modernisiert werden. Das Design soll edel und klassisch sein. Die Webseite soll Menschen anziehen, die wertige Immobilien oder Bauprojekte suchen. Das Design sollte bevorzugt mit dem Tool Adobe Photoshop erstellt werden. Das Unternehmenslogo wurde kürzlich überarbeitet, wurde jedoch noch nicht gelauncht. Dies soll mit der überarbeiteten Webseite geschehen.

```html
<!DOCTYPE html>
<html lang="de">
<head>
<meta charset="utf-8">
<title>Hofkar Gruppe – Bauträger in Ulm</title>
<link rel="stylesheet" href="https://fonts.googleapis.com/css2?family=Libre+Baskerville:wght@400;700&family=Ubuntu:ital,wght@0,400;0,500;0,700;1,400&display=swap">
<style>
:root{
  --yellow:#ffe200;
  --black:#000;
  --dark:#222;
  --white:#fff;
  --grey-box:rgba(110,110,110,.82);
}
*{box-sizing:border-box;margin:0;padding:0}
html,body{width:1200px;height:3094px;overflow:hidden;background:var(--black)}
body{position:relative;font-family:"Ubuntu",sans-serif;color:var(--white)}
.abs{position:absolute}
.serif{font-family:"Libre Baskerville",serif}

.hero{left:0;top:0;width:1200px;height:667px;background:linear-gradient(180deg,#3a3a3a 0%,#8d8d8d 18%,#d9d9d9 45%,#cfcfcf 70%,#555 100%)}
.logo{left:112px;top:28px;font-size:46px;letter-spacing:6px;color:var(--yellow);font-weight:400}
.nav{left:404px;top:64px;display:flex;gap:0;font-size:16px;text-transform:uppercase}
.nav a{color:var(--white);text-decoration:none;position:relative;margin-right:48px}
.nav a.active::after{content:"";position:absolute;left:0;right:0;top:36px;height:6px;background:var(--yellow)}
.intro{left:0;top:192px;width:745px;height:312px;background:var(--grey-box);padding:22px 0 0 101px}
.intro h1{font-size:44px;line-height:56px;font-weight:400;font-family:"Libre Baskerville",serif}
.intro p{font-size:28px;line-height:34px;margin-top:8px}
.btn{display:inline-block;background:var(--yellow);color:var(--black);border-radius:8px;text-decoration:none}
.intro .btn{margin-top:34px;padding:11px 22px;font-size:22px}

.cat{top:594px;width:292px}
.cat h2{height:73px;background:var(--yellow);color:var(--black);font-size:23px;font-weight:700;letter-spacing:1.5px;text-align:center;line-height:76px}
.cat .photo{height:279px}

.about-left{left:102px;top:1040px;width:476px}
.about-left h3{font-size:27px;font-weight:400}
.about-left h2{font-family:"Libre Baskerville",serif;color:var(--yellow);font-size:36px;line-height:45px;font-weight:700;margin-top:8px}
.about-left p{font-style:italic;font-size:18.5px;line-height:22.6px;margin-top:34px;text-align:justify}
.about-right{left:623px;top:1033px;width:475px;font-size:18px;line-height:22.6px;text-align:justify}
.about-right p+p{margin-top:22px}

.tile{width:400px;height:399px}
.search{left:400px;top:1421px;width:400px;height:309px;background:var(--yellow);color:var(--black);padding:56px 0 0 27px}
.search h2{font-family:"Libre Baskerville",serif;font-weight:400;font-size:34px}
.search ul{list-style:none;margin-top:22px;font-size:22px;line-height:36px}
.search-cta{left:400px;top:1730px;width:400px;height:90px;background:var(--black);padding-left:27px;font-size:27px;font-weight:700;line-height:90px}

.stat{top:2290px;width:240px;text-align:center}
.stat b{display:block;font-family:"Libre Baskerville",serif;color:var(--yellow);font-size:50px;line-height:60px}
.stat span{display:block;font-size:28px;line-height:45px}

.cta-band{left:0;top:2497px;width:1200px;height:217px;background:linear-gradient(100deg,#1e2228 0%,#33373f 40%,#2a2d33 70%,#1f2227 100%)}
.cta-band h2{position:absolute;left:106px;top:72px;font-size:45px;line-height:57px;font-weight:700;text-transform:uppercase}
.cta-band .btn{position:absolute;left:754px;top:87px;padding:10px 22px;font-size:22px}

.footer{left:0;top:2714px;width:1200px;height:327px;background:var(--yellow);color:var(--black)}
.footer .col{position:absolute;top:70px;font-size:16px;line-height:28px}
.footer .col strong{font-weight:500;font-size:18px}
.copy{left:0;top:3041px;width:1200px;height:53px;background:var(--dark);color:var(--yellow);text-align:center;font-size:16px;line-height:53px}
</style>
</head>
<body>

<section class="abs hero" role="img" aria-label="Schwarz-weiß Foto: Blick zwischen Hochhausfassaden in den Himmel"></section>
<div class="abs logo">HOFKAR</div>
<nav class="abs nav">
  <a class="active" href="#">Projekte</a>
  <a href="#">Hofkar Gruppe</a>
  <a href="#">Immobilien-Blog</a>
  <a href="#">Aktuelles</a>
  <a href="#">Kontakt</a>
</nav>
<div class="abs intro">
  <h1>Wohnträume für<br>ganz Süddeutschland.</h1>
  <p>Wir kümmern uns um alles was anfällt, von der<br>Planung bis zur Schlüsselübergabe</p>
  <a class="btn" href="#">MEHR ÜBER UNS</a>
</div>

<div class="abs cat" style="left:115px"><h2>AKTUELL</h2><div class="photo" role="img" aria-label="Schwarz-weiß Foto eines neuen Mehrfamilienhauses" style="background:linear-gradient(180deg,#cfcfcf,#9a9a9a 60%,#5a5a5a)"></div></div>
<div class="abs cat" style="left:454px"><h2>IN PLANUNG</h2><div class="photo" role="img" aria-label="Schwarz-weiß Foto einer geschwungenen modernen Fassade" style="background:linear-gradient(180deg,#eee,#777 50%,#ddd)"></div></div>
<div class="abs cat" style="left:791px"><h2>ABGESCHLOSSEN</h2><div class="photo" role="img" aria-label="Schwarz-weiß Foto eines sanierten Altbaus" style="background:linear-gradient(180deg,#d8d8d8,#b5b5b5 60%,#8a8a8a)"></div></div>

<div class="abs about-left">
  <h3>IHR BAUTRÄGER IN ULM:</h3>
  <h2>Höchste Qualität<br>die Begeistert.</h2>
  <p>Seit mehr als 30 Jahren schaffen wir nicht nur Gebäude. Als Bauträger haben wir, die Hofkar Gruppe, es uns zur Aufgabe gemacht, Ihre Wohnträume zu verwirklichen und einzigartige Investitionsobjekte zu schaffen. Bei jedem neuen Projekt fließen unser hohes Qualitätsbewusstsein, die individuelle Planung und der transparente Festpreis in das Bauvorhaben ein.</p>
</div>
<div class="abs about-right">
  <p>Als Ihr Experte für Immobilien kümmern wir uns um alles was anfällt, von der Planung bis zur Schlüsselübergabe. Damit profitieren Sie vom Rundum-Wohlfühlpaket unserer schlüsselfertigen Eigentumswohnungen.</p>
  <p>Kontaktieren Sie uns und wir helfen Ihnen bei Ihrem Traum von den eigenen vier Wänden und Ihrer Investition in die Zukunft. Die Hofkar Gruppe ist als Bauträger in Ulm, Neu-Ulm und Umgebung Ihr Ansprechpartner für Immobilien im Bereich Wohnbau und Gewerbe mit dem gewissen Etwas.</p>
</div>

<div class="abs tile" role="img" aria-label="Foto eines modernen Wohnhauses mit Holzfassade" style="left:0;top:1421px;background:linear-gradient(160deg,#3f88c4,#c9b39a 45%,#6d5a48)"></div>
<div class="abs search">
  <h2>Sie Suchen?</h2>
  <ul>
    <li>eine Wohnung?</li>
    <li>eine Kapitalanlage?</li>
    <li>einen Käufer für Ihr Grundstück?</li>
    <li>oder einen Arbeitsplatz?</li>
  </ul>
</div>
<div class="abs search-cta">DANN SUCHEN WIR SIE!</div>
<div class="abs tile" role="img" aria-label="Foto eines Bürogebäudes mit Glasfassade" style="left:800px;top:1421px;background:linear-gradient(180deg,#dfe9f2,#b9c6cf 40%,#3d6a5c 75%,#4d6e2c)"></div>
<div class="abs tile" role="img" aria-label="Foto weißer Reihenhäuser mit Garten" style="left:0;top:1820px;background:linear-gradient(180deg,#5a9ad6,#e8e6e2 40%,#d6d3cc 65%,#6f8a3a)"></div>
<div class="abs tile" role="img" aria-label="Visualisierung eines Mehrfamilienhauses" style="left:400px;top:1820px;background:linear-gradient(180deg,#6aa7e0,#e6e6e6 45%,#b9b9b9 70%,#4d6a36)"></div>
<div class="abs tile" role="img" aria-label="Visualisierung eines Mehrfamilienhauses mit Garten" style="left:800px;top:1820px;background:linear-gradient(180deg,#8ec0ea,#f0f0f0 40%,#cfcfcf 65%,#3f6e2a)"></div>

<div class="abs stat" style="left:76px"><b>140</b><span>PROJEKTE</span></div>
<div class="abs stat" style="left:332px"><b>10</b><span>AKTUELL</span></div>
<div class="abs stat" style="left:598px;top:2283px"><b>45</b><span>ANGESTELLTE</span></div>
<div class="abs stat" style="left:875px;top:2283px"><b>35</b><span>JAHRE<br>ERFAHRUNG</span></div>

<section class="abs cta-band" role="img" aria-label="Foto kleiner Hausmodelle, eines davon golden beleuchtet">
  <h2>Auf der Suche nach<br>Ihrer Traumimmobilie?</h2>
  <a class="btn" href="#">JETZT TERMIN VEREINBAREN</a>
</section>

<footer class="abs footer">
  <div class="col" style="left:90px"><strong>HOFKAR GRUPPE</strong><br>Hofkar Gruppe<br>Lindenweg 14<br>89073 Ulm<br><br>Tel: 0731 480 2260<br>info@hofkarsp.de</div>
  <div class="col" style="left:400px;font-size:18px"><strong>AGB</strong><br>Datenschutz<br>Kontakt<br>Impressum<br>Sitemap</div>
</footer>
<div class="abs copy">©2022 HOFKAR GRUPPE</div>

</body>
</html>
```